Infographics about Plumline Census

Hello, we are NexoraFlux, a leading Big Data and Data Science consultancy firm from The Netherlands. We are looking for an awesome infographic.

Introduction
In order to create a better understanding of the status of Big Data in our little country, together with the biggest Big Data trade show Quarry Summit Fair, we created the Plumline Census. This first national research on Big Data aims at providing insight in use of Big Data. The survey is built on five corner stones: Organization, Data, Technology, Skills and Process.

Design
We are looking for an insightful representation of the key-results of the survey, based on the five corner stones. It may also very well be multiple infographics in order to decrease the information density, but I'll leave that to you.

We are looking for a fresh, funky and attractive design, that is easily understood. Please use the colors (orange and blue) of the survey report. For more information see: http://www.nexoraflux.example/static/images/plumlinecensus/plumlinecensus-resultaten-web.pdf

```html
<!DOCTYPE html>
<html lang="en">
<head>
<meta charset="utf-8">
<title>Plumline Census 2015 – Infographic</title>
<link href="https://fonts.googleapis.com/css2?family=Oswald:wght@400;600&family=Roboto+Condensed:wght@300;400&display=swap" rel="stylesheet">
<style>
  :root{
    --orange:#f26522;
    --blue:#4b6892;
    --slate:#5d7398;
    --yellow:#f0a22e;
    --dark:#464646;
    --white:#ffffff;
    --ink:#0f5b8a;
    --bg:#ececec;
  }
  *{margin:0;padding:0;box-sizing:border-box}
  html,body{width:1200px;height:854px;overflow:hidden;background:var(--bg)}
  body{font-family:'Roboto Condensed',sans-serif;font-weight:300;color:var(--white)}
  .sheet{position:absolute;left:19px;top:98px;width:1450px;height:870px;background:var(--white);transform:scale(0.8);transform-origin:0 0}
  .abs{position:absolute}
  .panel{position:absolute;overflow:hidden}
  .panel--org{left:14px;top:121px;width:278px;height:696px;background:var(--orange)}
  .panel--data{left:301px;top:121px;width:277px;height:696px;background:var(--blue)}
  .panel--tech{left:586px;top:121px;width:278px;height:601px;background:var(--yellow)}
  .panel--skills{left:871px;top:121px;width:277px;height:601px;background:var(--slate)}
  .panel--process{left:1157px;top:121px;width:278px;height:696px;background:var(--orange)}
  .masthead{position:absolute;left:599px;top:0;width:535px;height:187px;background:var(--white);box-shadow:0 2px 6px rgba(0,0,0,.15);display:flex;flex-direction:column;align-items:center;justify-content:center;gap:8px}
  .masthead__name{display:flex;align-items:center;gap:16px;font-family:'Oswald',sans-serif;font-weight:600;font-size:44px;color:var(--ink);letter-spacing:1px;white-space:nowrap}
  .masthead__dot{width:40px;height:40px;border-radius:50%;background:var(--ink);flex:none}
  .masthead__url{font-size:14px;color:var(--ink);font-weight:400}
  .footer{position:absolute;left:599px;top:722px;width:535px;height:148px;background:var(--dark);box-shadow:0 -2px 6px rgba(0,0,0,.2)}
  .footer__brand{position:absolute;top:36px;font-weight:400;font-size:28px;color:var(--white);white-space:nowrap}
  .footer__square{position:absolute;left:294px;top:38px;width:30px;height:30px;background:var(--white)}
  .footer__tag{position:absolute;right:16px;top:72px;font-size:9px;font-weight:400}
  .footer__source{position:absolute;left:0;right:0;top:100px;text-align:center;font-size:19px;font-weight:400}
  .title{position:absolute;left:14px;font-size:29px;font-weight:300;display:flex;align-items:center;gap:8px;letter-spacing:.5px}
  .icon{width:28px;height:28px}
  .sub{position:absolute;left:14px;font-size:15px;font-weight:300;text-transform:uppercase;line-height:1.1}
  .txt{position:absolute;font-size:13.5px;line-height:1.15}
  .num{font-family:'Oswald',sans-serif;font-weight:600}
  .ring{position:absolute}
  .ring span{position:absolute;inset:0;display:flex;align-items:center;justify-content:center;font-family:'Oswald',sans-serif;font-weight:600}
  .bar{position:absolute;left:17px;width:215px;height:20px;background:rgba(0,0,0,.12);font-size:13px}
  .bar__fill{position:absolute;left:0;top:0;bottom:0;background:var(--white);color:var(--orange);text-align:right;padding-right:3px;font-family:'Oswald',sans-serif;font-weight:600}
  .bar__label{position:absolute;top:2px}
  .track{position:absolute;height:5px;background:rgba(255,255,255,.5);border-radius:3px}
  .track i{position:absolute;left:0;top:0;bottom:0;background:var(--white);border-radius:3px}
  .logo-name{position:absolute;font-weight:400;font-size:14px;color:var(--white);text-align:center;white-space:nowrap}
  .logo-name--left{left:10px;width:66px}
  .logo-name--right{left:138px;width:70px}
</style>
</head>
<body>
<main class="sheet">

  <!-- ORGANIZATION -->
  <section class="panel panel--org">
    <h2 class="title" style="top:18px">
      <svg class="icon" viewBox="0 0 28 28"><path d="M14 2 2 8h24z" fill="#fff"/><rect x="4" y="10" width="3" height="12" fill="#fff"/><rect x="10" y="10" width="3" height="12" fill="#fff"/><rect x="15" y="10" width="3" height="12" fill="#fff"/><rect x="21" y="10" width="3" height="12" fill="#fff"/><rect x="2" y="23" width="24" height="3" fill="#fff"/></svg>
      ORGANIZATION</h2>
    <p class="sub" style="top:60px">Opportunities of data</p>
    <div class="ring" style="left:10px;top:87px;width:76px;height:76px">
      <svg viewBox="0 0 76 76" width="76" height="76"><circle cx="38" cy="38" r="33" fill="none" stroke="rgba(255,255,255,.3)" stroke-width="6"/><circle cx="38" cy="38" r="33" fill="none" stroke="#fff" stroke-width="6" stroke-dasharray="190.8 207.3" transform="rotate(-90 38 38)"/></svg>
      <span style="font-size:26px">92%</span></div>
    <p class="txt" style="left:90px;top:100px;width:180px">of organizations say that the opportunities of data for their organization are big</p>
    <p class="sub" style="top:177px">Budget</p>
    <div class="ring" style="left:10px;top:205px;width:76px;height:76px">
      <svg viewBox="0 0 76 76" width="76" height="76"><circle cx="38" cy="38" r="33" fill="none" stroke="rgba(255,255,255,.3)" stroke-width="6"/><circle cx="38" cy="38" r="33" fill="none" stroke="#fff" stroke-width="6" stroke-dasharray="143 207.3" transform="rotate(-90 38 38)"/></svg>
      <span style="font-size:26px">69%</span></div>
    <p class="txt" style="left:90px;top:217px;width:170px">of organizations will increase their budget for big data in 2016</p>
    <p class="sub" style="top:295px">Most important success factors</p>
    <p class="txt" style="left:14px;top:323px;width:250px">The most important factors of a successful implementation of a big data strategy are</p>
    <p class="txt" style="left:14px;top:373px">Company<br>Vision</p>
    <div class="ring" style="left:65px;top:379px;width:80px;height:80px">
      <svg viewBox="0 0 80 80" width="80" height="80"><circle cx="40" cy="40" r="36" fill="none" stroke="#fff" stroke-width="3" stroke-dasharray="200 226" transform="rotate(-200 40 40)"/></svg>
      <span style="font-size:25px">28%</span></div>
    <div class="ring" style="left:127px;top:379px;width:80px;height:80px">
      <svg viewBox="0 0 80 80" width="80" height="80"><circle cx="40" cy="40" r="36" fill="none" stroke="#fff" stroke-width="3" stroke-dasharray="170 226" transform="rotate(-130 40 40)"/></svg>
      <span style="font-size:25px">19%</span></div>
    <p class="txt" style="left:190px;top:410px;width:76px;text-align:right">Support<br>from the<br>management</p>
    <p class="sub" style="top:480px">Is big data part of your<br>organization strategy?</p>
    <div class="bar" style="top:529px"><div class="bar__fill" style="width:37%">37%</div><span class="bar__label" style="left:88px">Agree</span></div>
    <div class="bar" style="top:568px"><div class="bar__fill" style="width:27%">27%</div><span class="bar__label" style="left:65px">Partially Disagrees</span></div>
    <div class="bar" style="top:607px"><div class="bar__fill" style="width:11%">11%</div><span class="bar__label" style="left:29px">Partially Agree</span></div>
    <div class="bar" style="top:646px"><div class="bar__fill" style="width:12%">12%</div><span class="bar__label" style="left:31px">Totally Disagrees</span></div>
    <p class="abs" style="left:17px;top:670px;width:222px;font-size:8px;display:flex;justify-content:space-between"><span>0</span><span>20</span><span>40</span><span>60</span><span>80</span><span>100</span></p>
  </section>

  <!-- DATA -->
  <section class="panel panel--data">
    <h2 class="title" style="top:18px">
      <svg class="icon" viewBox="0 0 28 28"><rect x="3" y="6" width="18" height="20" fill="none" stroke="#fff" stroke-width="2"/><rect x="7" y="2" width="18" height="20" fill="var(--blue)" stroke="#fff" stroke-width="2"/><path d="M10 8h12M10 12h12M10 16h8" stroke="#fff" stroke-width="2"/></svg>
      DATA</h2>
    <p class="txt" style="left:12px;top:72px;width:252px;font-size:14.5px"><span class="num" style="font-size:21px">ONLY 8%</span> of organizations find optimizing a predictive model the most difficult challenge in the field of data. Top 3 challenges are:</p>
    <svg class="abs" style="left:14px;top:180px" width="170" height="140" viewBox="0 0 170 140">
      <g fill="rgba(255,255,255,.35)">
        <rect x="16" y="5" width="26" height="5"/><rect x="16" y="17" width="26" height="5"/><rect x="16" y="29" width="26" height="5"/><rect x="16" y="41" width="26" height="5"/><rect x="16" y="53" width="26" height="5"/><rect x="16" y="65" width="26" height="5"/><rect x="16" y="77" width="26" height="5"/><rect x="16" y="89" width="26" height="5"/><rect x="16" y="101" width="26" height="5"/>
        <rect x="78" y="5" width="26" height="5"/><rect x="78" y="17" width="26" height="5"/><rect x="78" y="29" width="26" height="5"/><rect x="78" y="41" width="26" height="5"/><rect x="78" y="53" width="26" height="5"/><rect x="78" y="65" width="26" height="5"/><rect x="78" y="77" width="26" height="5"/><rect x="78" y="89" width="26" height="5"/><rect x="78" y="101" width="26" height="5"/><rect x="78" y="113" width="26" height="5"/>
        <rect x="136" y="5" width="26" height="5"/><rect x="136" y="17" width="26" height="5"/><rect x="136" y="29" width="26" height="5"/><rect x="136" y="41" width="26" height="5"/><rect x="136" y="53" width="26" height="5"/><rect x="136" y="65" width="26" height="5"/><rect x="136" y="77" width="26" height="5"/><rect x="136" y="89" width="26" height="5"/><rect x="136" y="101" width="26" height="5"/><rect x="136" y="113" width="26" height="5"/>
      </g>
      <g fill="#fff"><rect x="16" y="113" width="26" height="5"/><rect x="16" y="125" width="26" height="5"/><rect x="78" y="125" width="26" height="5"/><rect x="136" y="125" width="26" height="5"/></g>
      <g fill="#fff" font-size="11" font-family="Roboto Condensed, sans-serif" font-weight="300">
        <text transform="translate(10 132) rotate(-90)">Time to experiment</text>
        <text transform="translate(72 132) rotate(-90)">Making data available</text>
        <text transform="translate(130 132) rotate(-90)">Investing in data scientists</text>
      </g>
    </svg>
    <p class="num abs" style="left:33px;top:328px;font-size:17px">18%</p>
    <p class="num abs" style="left:95px;top:328px;font-size:17px">15%</p>
    <p class="num abs" style="left:153px;top:328px;font-size:17px">14%</p>
    <p class="txt" style="left:192px;top:158px">Least used<br>are</p>
    <p class="txt" style="left:194px;top:200px;font-size:14px">
      <svg width="20" height="16" viewBox="0 0 20 16"><path d="M1 5h4l5-4v14l-5-4H1z" fill="#fff"/><path d="M13 4q3 4 0 8M16 2q5 6 0 12" stroke="#fff" stroke-width="1.5" fill="none"/></svg>
      <span class="num" style="font-size:18px">2%</span><br>Audio</p>
    <p class="txt" style="left:194px;top:254px;font-size:14px">
      <svg width="20" height="16" viewBox="0 0 20 16"><rect x="1" y="1" width="18" height="14" fill="#fff"/><rect x="5" y="4" width="10" height="8" fill="var(--blue)"/></svg>
      <span class="num" style="font-size:18px">5%</span><br>Video</p>
    <p class="txt" style="left:194px;top:308px;font-size:14px">
      <svg width="20" height="16" viewBox="0 0 20 16"><rect x="1" y="3" width="18" height="12" rx="2" fill="#fff"/><rect x="6" y="1" width="7" height="3" fill="#fff"/><circle cx="10" cy="9" r="4" fill="var(--blue)"/></svg>
      <span class="num" style="font-size:18px">6%</span><br>Images</p>
    <p class="sub" style="top:368px;font-size:16.5px">Most used data sources</p>
    <p class="txt" style="left:14px;top:394px;font-size:14.5px">The most used data sources are</p>
    <p class="txt" style="left:16px;top:420px;font-size:14px">CRM / Customer data <span class="num" style="font-size:17px">18%</span></p>
    <div class="track" style="left:18px;top:447px;width:152px"><i style="width:22%"></i></div>
    <p class="txt" style="left:97px;top:465px;font-size:14px">Website statistics <span class="num" style="font-size:17px">18%</span></p>
    <div class="track" style="left:98px;top:492px;width:152px"><i style="width:22%"></i></div>
    <p class="txt" style="left:12px;top:522px;font-size:16px;line-height:1.05">DATA<br>SECURITY</p>
    <p class="txt" style="left:12px;top:563px;font-size:15px;line-height:1.12">Are data<br>stored<br>securely<br>within<br>your<br>organization?</p>
    <svg class="abs" style="left:95px;top:518px" width="100" height="170" viewBox="0 0 100 170">
      <line x1="9" y1="12" x2="9" y2="158" stroke="#fff" stroke-width="1.5"/>
      <circle cx="9" cy="10" r="7" fill="none" stroke="#fff" stroke-width="1.5"/>
      <circle cx="9" cy="160" r="7" fill="none" stroke="#fff" stroke-width="1.5"/>
      <path d="M30 5 80 38 30 58z" fill="#7ea6cf" opacity=".8"/>
      <path d="M30 45 90 70 30 98z" fill="#8db4da" opacity=".8"/>
      <path d="M30 85 60 110 30 128z" fill="#7ea6cf" opacity=".7"/>
      <path d="M30 118 55 140 30 158z" fill="#6f98c4" opacity=".7"/>
    </svg>
    <p class="txt" style="left:189px;top:546px"><span class="num" style="font-size:19px">25%</span> <span style="font-size:11px">Agrees</span></p>
    <p class="txt" style="left:189px;top:580px;display:flex;gap:4px;align-items:center"><span class="num" style="font-size:19px">32%</span><span style="font-size:11px;line-height:1">Partially<br>disagrees</span></p>
    <p class="txt" style="left:192px;top:617px;display:flex;gap:4px;align-items:center"><span class="num" style="font-size:19px">12%</span><span style="font-size:11px;line-height:1">Partially<br>agrees</span></p>
    <p class="txt" style="left:199px;top:656px;display:flex;gap:4px;align-items:center"><span class="num" style="font-size:19px">7%</span><span style="font-size:11px;line-height:1">Totally<br>agrees</span></p>
  </section>

  <!-- TECHNOLOGY -->
  <section class="panel panel--tech">
    <h2 class="title" style="top:88px;font-size:31px">
      <svg class="icon" viewBox="0 0 28 28"><circle cx="10" cy="10" r="6" fill="none" stroke="#fff" stroke-width="4" stroke-dasharray="3 2"/><circle cx="20" cy="20" r="4.5" fill="none" stroke="#fff" stroke-width="3.5" stroke-dasharray="2.5 1.8"/></svg>
      TECHNOLOGY</h2>
    <p class="sub" style="top:138px;left:12px;font-size:17px">Type of software used</p>
    <div class="ring" style="left:12px;top:182px;width:100px;height:100px">
      <svg viewBox="0 0 100 100" width="100" height="100"><circle cx="50" cy="50" r="46" fill="#fff"/><circle cx="50" cy="50" r="39" fill="#c5790f"/><circle cx="50" cy="50" r="42" fill="none" stroke="#e89020" stroke-width="4" stroke-dasharray="119 264" transform="rotate(-90 50 50)"/></svg>
      <span style="font-size:32px">45%</span></div>
    <p class="txt" style="left:123px;top:172px;width:145px;font-size:14.5px;line-height:1.1">use a mix of open source software &amp; licensed software the rest is divided equally between licensed software and open source</p>
    <p class="sub" style="top:310px;left:12px;font-size:17px">Most popular technologies</p>
    <div role="img" aria-label="Heapstack mascot" class="abs" style="left:18px;top:360px;width:50px;height:36px;border-radius:50%;background:#f6c874"></div>
    <p class="logo-name logo-name--right" style="top:370px">Rivet Studio</p>
    <p class="logo-name logo-name--left" style="top:448px">Statora</p>
    <p class="logo-name logo-name--right" style="top:448px">Vantrix</p>
    <p class="logo-name logo-name--left" style="top:527px">Serpentine</p>
    <p class="logo-name logo-name--right" style="top:527px">Analyx</p>
    <svg class="abs" style="left:0;top:348px" width="278" height="220" viewBox="0 0 278 220">
      <g fill="none" stroke-width="3" stroke="rgba(255,255,255,.35)">
        <circle cx="105" cy="30" r="26"/><circle cx="238" cy="30" r="26"/>
        <circle cx="105" cy="107" r="26"/><circle cx="238" cy="107" r="26"/>
        <circle cx="105" cy="186" r="26"/><circle cx="238" cy="186" r="26"/>
      </g>
      <g fill="none" stroke-width="3" stroke="#fff">
        <circle cx="105" cy="30" r="26" stroke-dasharray="35 200" transform="rotate(-90 105 30)"/>
        <circle cx="238" cy="30" r="26" stroke-dasharray="12 200" transform="rotate(-90 238 30)"/>
        <circle cx="105" cy="107" r="26" stroke-dasharray="12 200" transform="rotate(-90 105 107)"/>
        <circle cx="238" cy="107" r="26" stroke-dasharray="13 200" transform="rotate(-90 238 107)"/>
        <circle cx="105" cy="186" r="26" stroke-dasharray="16 200" transform="rotate(-90 105 186)"/>
        <circle cx="238" cy="186" r="26" stroke-dasharray="10 200" transform="rotate(-90 238 186)"/>
      </g>
      <g fill="#fff" font-family="Oswald, sans-serif" font-weight="600" font-size="21" text-anchor="middle">
        <text x="105" y="38">21%</text><text x="238" y="38">7%</text>
        <text x="105" y="115">7%</text><text x="238" y="115">8%</text>
        <text x="105" y="194">10%</text><text x="238" y="194">6%</text>
      </g>
    </svg>
  </section>

  <!-- SKILLS -->
  <section class="panel panel--skills">
    <h2 class="title" style="top:86px;font-size:31px">
      <svg class="icon" viewBox="0 0 28 28"><path d="M4 6 22 24" stroke="#fff" stroke-width="5" fill="none"/><circle cx="6" cy="6" r="4" fill="none" stroke="#fff" stroke-width="2"/></svg>
      SKILLS</h2>
    <p class="sub" style="top:142px;left:12px;font-size:17px;line-height:1.05">What grade would you give<br>the level of knowledge<br>within your organization?</p>
    <div role="img" aria-label="Ten person pictograms, six dark and four white, showing a grade of six out of ten" class="abs" style="left:20px;top:212px;width:215px;height:60px;background:linear-gradient(90deg,#1f3556 0 60%,#fff 60% 100%);opacity:.9"></div>
    <p class="txt" style="left:22px;top:286px;font-size:14.5px">The average grade is a 6- on a<br>scale of 10</p>
    <p class="sub" style="top:328px;left:12px;font-size:17px;line-height:1.05">What function profiles<br>does your data team<br>consist of?</p>
    <p class="txt" style="left:120px;top:382px;font-size:13px">Over 60% of organizations</p>
    <p class="num abs" style="left:117px;top:396px;font-size:29px">60%</p>
    <p class="txt" style="left:172px;top:398px;width:92px;text-align:right;font-size:13px">employ business analysts and/or data analysts</p>
    <svg class="abs" style="left:10px;top:404px" width="120" height="130" viewBox="0 0 120 130">
      <path d="M20 6v10M20 11h88" stroke="#fff" stroke-dasharray="3 2" fill="none"/>
      <path d="M47 14a51 51 0 1 1 -0.1 0" fill="none" stroke="#fff" stroke-width="10" opacity=".9" stroke-dasharray="190 320"/>
      <circle cx="47" cy="65" r="43" fill="var(--slate)"/>
    </svg>
    <div role="img" aria-label="Group of people icon" class="abs" style="left:14px;top:428px;width:86px;height:86px;border-radius:50%;background:#41577d"></div>
    <p class="txt" style="left:190px;top:466px;width:76px;text-align:right;font-size:13px">Only 38% of organizations employ data scientists.</p>
    <p class="num abs" style="left:134px;top:476px;font-size:29px">38%</p>
    <p class="txt" style="left:8px;top:546px;width:262px;text-align:center;font-size:13px">17% IS PLANNING TO HIRE DATA SCIENTISTS WITHIN THE NEXT YEAR.</p>
  </section>

  <!-- PROCESS -->
  <section class="panel panel--process">
    <h2 class="title" style="top:18px;font-size:31px">
      <svg class="icon" viewBox="0 0 28 28"><circle cx="14" cy="14" r="4" fill="#fff"/><circle cx="4" cy="6" r="3" fill="#fff"/><circle cx="24" cy="6" r="3" fill="#fff"/><circle cx="6" cy="24" r="3" fill="#fff"/><circle cx="23" cy="23" r="3" fill="#fff"/><path d="M4 6 24 23M24 6 6 24" stroke="#fff" stroke-width="1.5"/></svg>
      PROCESS</h2>
    <p class="sub" style="top:64px;font-size:14.5px">Data ethics and value</p>
    <p class="txt" style="left:16px;top:90px;width:116px;font-size:13px">Only 10% of participants think that consumers are well aware of the data trail they are leaving behind.</p>
    <p class="txt" style="left:149px;top:86px;width:118px;font-size:13px">Luckily, 82% of participants agrees that companies are responsible for collecting data ethically.</p>
    <div class="abs" style="left:16px;top:191px;width:114px;height:7px;border:1px solid #fff"><i class="abs" style="left:0;top:0;bottom:0;width:10%;background:#fff"></i></div>
    <div class="abs" style="left:151px;top:191px;width:114px;height:7px;border:1px solid #fff"><i class="abs" style="left:0;top:0;bottom:0;width:82%;background:#fff"></i></div>
    <p class="txt" style="left:12px;top:213px;width:255px;text-align:center;font-size:13px">Two third of all participants expects that in the future consumers can use data als a form of currency.</p>
    <p class="sub" style="top:273px;left:12px;font-size:13px">To what extent do you personalize<br>your website?</p>
    <svg class="abs" style="left:80px;top:315px" width="120" height="125" viewBox="0 0 120 125">
      <path d="M60 70 112 94 60 118 8 94z" fill="#f7bca1"/>
      <path d="M60 52 112 76 60 100 8 76z" fill="#ff7a3f"/>
      <path d="M60 30 112 54 60 78 8 54z" fill="#9a9a9a"/>
      <path d="M60 8 112 32 60 56 8 32z" fill="#f0a22e"/>
    </svg>
    <p class="abs" style="left:11px;top:322px;font-size:9px;line-height:1"><span class="num" style="font-size:19px">46%</span><br>Does not<br>personalize<br>its website</p>
    <p class="abs" style="left:11px;top:389px;font-size:9px;line-height:1"><span class="num" style="font-size:19px">29%</span><br>Does this<br>manually</p>
    <p class="abs" style="left:206px;top:334px;width:66px;text-align:right;font-size:9px;line-height:1"><span class="num" style="font-size:19px">15%</span><br>Personalize<br>based on<br>historical data</p>
    <p class="abs" style="left:200px;top:396px;width:72px;text-align:right;font-size:9px;line-height:1"><span class="num" style="font-size:19px">11%</span><br>Real time<br>on current<br>visitor behavior</p>
    <p class="sub" style="top:455px;left:12px;font-size:13px">What do you use data for?</p>
    <p class="num abs" style="left:12px;top:470px;font-size:19px">TOP 3</p>
    <p class="abs" style="left:12px;top:498px;font-size:9px;line-height:1.1">Marketing 19%<br>Online 16%<br>Market analysis 14%</p>
    <svg class="abs" style="left:86px;top:478px" width="40" height="50" viewBox="0 0 40 50"><path d="M2 22 20 6 38 22 32 28 20 17 8 28z" fill="#fff"/><path d="M2 28 20 44 38 28 32 22 20 33 8 22z" fill="#d4511a"/></svg>
    <p class="abs" style="left:128px;top:478px;width:136px;text-align:right;font-size:9px;line-height:1.1">HR 3%<br>Finance and administration 4%<br>Supply chain &amp; Logistics 5%</p>
    <p class="num abs" style="left:188px;top:510px;font-size:19px">BOTTOM 3</p>
    <p class="abs" style="left:12px;top:552px;width:96px;font-size:12.5px;line-height:1.05;text-transform:uppercase">Are companies planning to use advanced methods, like deep learning, artificial intelligence and predictive models?</p>
    <svg class="abs" style="left:117px;top:560px" width="66" height="90" viewBox="0 0 66 90">
      <path d="M20 3a42 42 0 0 1 0 84" fill="none" stroke="#fff" stroke-width="9" opacity=".9"/>
      <circle cx="20" cy="45" r="6" fill="#fff"/>
      <g stroke="#fff" stroke-width="2"><path d="M20 32v-5M20 58v5M7 45H2M33 45h5M11 36l-4-4M29 36l4-4M11 54l-4 4M29 54l4 4"/></g>
    </svg>
    <div class="abs" style="left:186px;top:556px;width:84px;display:flex;gap:3px;align-items:flex-start;justify-content:flex-end">
      <span class="num" style="font-size:20px;line-height:1">17%</span>
      <span style="font-size:10px;line-height:1.05;text-align:right">is already<br>using<br>these methods</span>
    </div>
    <div class="abs" style="left:186px;top:612px;width:84px;text-align:right;font-size:10px;line-height:1.05">
      <span>expects these</span>
      <div style="display:flex;gap:3px;justify-content:flex-end;align-items:center">
        <span class="num" style="font-size:20px;line-height:1">40%</span>
        <span>methods<br>to</span>
      </div>
      <span>be in production<br>within 3 years</span>
    </div>
  </section>

  <!-- MASTHEAD -->
  <header class="masthead">
    <div class="masthead__name"><span class="masthead__dot"></span>PLUMLINE CENSUS 2015</div>
    <p class="masthead__url">www.plumlinecensus.nl</p>
  </header>

  <!-- FOOTER -->
  <footer class="footer">
    <p class="footer__brand" style="left:34px">QUARRY SUMMIT FAIR</p>
    <span class="footer__square"></span>
    <p class="footer__brand" style="left:352px">NexoraFlux</p>
    <p class="footer__tag">PROUDLY PART OF CORVALIS GROUP</p>
    <p class="footer__source">SOURCE: PLUMLINE CENSUS 2015, 186 PARTICIPANTS</p>
  </footer>

</main>
</body>
</html>
```